Virtual assistant company needs letterhead and email signature

We need a letterhead and email signature for our virtual assistant company - dayBramble (small w capital F). Our tag line is think ahead | dayBramble

The colours we would like used are;

#81788c
#dddbe1

For reference our business cards have used #81788c background colour and #dddbe1 text

The fonts we would like used are

Lora
Proxima Nova

Please check out our twitter and facebook for style and feel

Twitter: @daybramble
www.chatterlane.com/daybramble

Please also find attached our landing page and business cards for reference

Any questions please let us know

Thanks
E

Reason: We like the opportunity to receive furthur designs

```html
<!DOCTYPE html>
<html lang="en">
<head>
<meta charset="utf-8">
<title>dayBramble Letterhead</title>
<link rel="stylesheet" href="https://fonts.googleapis.com/css2?family=Lora:wght@400&family=Montserrat:wght@400;500&family=Tinos:wght@400;700&display=swap">
<style>
  :root {
    --plum: #81788c;
    --mist: #dddbe1;
    --paper: #f4f4f5;
    --backdrop: #ebebec;
    --ink: #2b2b2e;
    --ink-soft: #55545b;
  }
  * { box-sizing: border-box; margin: 0; padding: 0; }
  html, body {
    width: 960px;
    height: 1200px;
    overflow: hidden;
    background: var(--backdrop);
  }
  .letterhead {
    position: absolute;
    left: 77px;
    top: 34px;
    width: 806px;
    height: 1131px;
    background: var(--plum);
    padding: 11px 11px 0 11px;
  }
  .sheet {
    position: relative;
    width: 100%;
    height: 1047px;
    background: var(--paper);
  }
  .brand {
    position: absolute;
    left: 52px;
    top: 48px;
  }
  .brand-name {
    font-family: "Lora", serif;
    font-weight: 400;
    font-size: 34px;
    line-height: 1;
    color: var(--plum);
    letter-spacing: 0.2px;
  }
  .brand-tagline {
    font-family: "Montserrat", sans-serif;
    font-size: 11.5px;
    color: var(--plum);
    margin-top: 3px;
    padding-left: 22px;
    letter-spacing: 0.3px;
  }
  .address {
    position: absolute;
    right: 59px;
    top: 60px;
    text-align: right;
    font-family: "Montserrat", sans-serif;
    font-size: 8.5px;
    line-height: 13px;
    color: var(--plum);
    letter-spacing: 0.5px;
    text-transform: uppercase;
  }
  .letter {
    position: absolute;
    left: 125px;
    right: 59px;
    top: 180px;
    font-family: "Tinos", serif;
    font-size: 10.8px;
    line-height: 23px;
    color: var(--ink);
  }
  .letter-meta strong { font-weight: 700; }
  .letter-body p {
    text-align: justify;
    margin-bottom: 23px;
  }
  .signoff {
    position: absolute;
    left: 125px;
    top: 588px;
    font-family: "Tinos", serif;
    font-size: 10.8px;
    line-height: 15px;
    color: var(--ink);
  }
  .signature {
    position: absolute;
    left: 125px;
    top: 632px;
    width: 214px;
    height: 126px;
    border-radius: 6px;
    background: linear-gradient(135deg, #e4e3e7, #ecebee);
  }
  .footer-band {
    position: absolute;
    left: 0;
    bottom: 0;
    width: 806px;
    height: 73px;
    background: linear-gradient(180deg, #857c90, var(--plum));
  }
</style>
</head>
<body>
  <div class="letterhead">
    <div class="sheet">
      <header class="brand">
        <div class="brand-name">dayBramble</div>
        <div class="brand-tagline">think ahead | dayBramble</div>
      </header>
      <address class="address" style="font-style:normal">
        418 Lantern Avenue, Suite 900<br>
        Brookvale, NY 10482
      </address>

      <section class="letter">
        <div class="letter-meta">
          <div><strong>Data : </strong><strong>Mon , 25 / 3 / 2013</strong></div>
          <div><strong>Recipient : </strong><strong>Mr.John Doe Sanderson</strong></div>
          <div>Dear Mr. Jhon Doe</div>
        </div>
        <div class="letter-body">
          <p>LoTrem ipsum dolor sit amet, consectetur adipiscing elit. Praesent vulputate, neque ac accumsan suscipit, justo turpis volutpat nisl, tempus fermentum eros tortor et elit. Vivamus porttitor faucibus gravida. Quisque pharetra gravida luctus. Donec eget turpis libero. Ut ac dolor urna, quis tempor nunc. Donec vitae mauris purus, euismod eleifend nulla. Lorem ipsum dolor sit amet, consectetur adipiscing elit. Donec ut purus tellus. Aenean quis dignissim lacus. Vestibulum suscipit vehicula cursus. Suspendisse potenti. Ut in sem nisi. Sed et massa leo.</p>
          <p>Fusce varius libero vel risus condimentum suscipit. Nullam tristique ultrices massa a volutpat. Donec sed dictum metus. Curabitur fringilla nibh eu ligula pharetra a interdum quam aliquam. Maecenas aliquam elit eu orci rutrum molestie. Proin nisl justo, varius a volutpat nec, ultricies sed sem. Nam sit amet imperdiet sem. Phasellus vitae mauris odio. Etiam in purus dui. Etiam ultricies, ante vel iaculis sodales, arcu leo adipiscing leo, sit amet mollis dui nisi non quam.</p>
          <p>Suspendisse sagittis laoreet dolor, vitae rhoncus arcu volutpat quis. Vestibulum at placerat dolor. Vivamus eu lacus ut enim molestie consectetur. Quisque ac lorem vel orci sagittis sollicitudin. Nunc ut quam sem, quis volutpat libero. Cum sociis natoque penatibus et magnis dis parturient montes, nascetur ridiculus mus. Vestibulum ante ipsum primis in faucibus orci luctus et ultrices posuere cubilia Curae; Donec tempor velit in velit feugiat sit amet vulputate nisl posuere..</p>
        </div>
      </section>

      <div class="signoff">
        <div>JOHN DOE</div>
        <div>General director</div>
      </div>
      <div class="signature" role="img" aria-label="Handwritten signature of the general director"></div>
    </div>
    <div class="footer-band" role="img" aria-label="Band of hand-drawn business sketches: charts, arrows and a product label"></div>
  </div>
</body>
</html>
```